New Billboard Design Project

I would like to have a banner made which is approx 16ft wide x 8ft tall showing our 3 businesses. I would like to use the new Ridgeline Depot Logo as the main , and have them all incorporated in one banner. I would like to have a nice background that would go with construction, excavation and material supply yard which sells landscape materials,
Updates

Adding photos to be incorporated

Target Market(s)

contractors, homeowners, landscapers, developers

Industry/Entity Type

Construction, land clearing, concrete foundations, Excaavation

Requirements
Must have
• excavation, concrete, all three logos

```html
<!DOCTYPE html>
<html lang="en">
<head>
<meta charset="utf-8">
<title>Ridgeline Depot Billboard</title>
<link href="https://fonts.googleapis.com/css2?family=Arimo:wght@400;700&display=swap" rel="stylesheet">
<style>
  :root {
    --page: #eef0f2;
    --panel-light: #f4f4f4;
    --panel-grey: #d9d9d9;
    --panel-band: #cfcfcf;
    --ink: #141414;
    --maroon: #7a2a20;
    --partner-red: #b3262b;
    --leaf: #2f8a3a;
    --seedling-frame: #8ab86a;
    --teal: #3fb7c0;
    --frame: #7d7d7d;
  }
  * { box-sizing: border-box; margin: 0; padding: 0; }
  html, body {
    width: 1200px; height: 800px; overflow: hidden;
    background: var(--page);
    font-family: "Arimo", Arial, sans-serif;
  }
  .billboard {
    position: absolute; left: 40px; top: 72px;
    width: 1120px; height: 656px;
    background: var(--panel-grey);
    overflow: hidden;
  }
  .billboard__backdrop { position: absolute; inset: 0; }
  .brand {
    position: absolute; left: 24px; top: 194px;
    display: flex; align-items: center; gap: 14px;
    color: var(--maroon); font-weight: 700;
    font-size: 54px; letter-spacing: 1px; line-height: 1;
  }
  .brand__dot {
    width: 48px; height: 48px; border-radius: 50%;
    background: var(--leaf); flex: none;
  }
  .contact {
    position: absolute; right: 20px; top: 56px; text-align: right; color: var(--ink);
  }
  .contact__label { font-size: 25px; font-weight: 700; line-height: 1.15; }
  .contact__phone { font-size: 58px; font-weight: 700; margin-top: 16px; letter-spacing: 1px; line-height: 1.15; }
  .offer {
    position: absolute; right: 20px; top: 203px;
    font-size: 21px; font-weight: 700; color: var(--ink);
  }
  .partner {
    position: absolute; left: 2px; width: 205px;
    background: #fff; border: 3px solid var(--partner-red);
    display: flex; flex-direction: column; justify-content: center; align-items: center;
    text-align: center; color: var(--partner-red);
    font-weight: 700; font-size: 21px; line-height: 1.2; padding: 8px;
  }
  .partner--excavation { top: 288px; height: 148px; }
  .partner--homes { top: 442px; height: 138px; }
  .photo { position: absolute; }
  .photo--seedlings {
    left: 213px; top: 279px; width: 212px; height: 296px;
    background:
      radial-gradient(ellipse 40% 30% at 55% 62%, rgba(214,170,150,0.55), rgba(214,170,150,0) 100%),
      linear-gradient(90deg, #2e4a26 0%, #4f8a3a 20%, #2a3a22 40%, #4f8a3a 60%, #2a3a22 80%, #4a7e36 100%);
    border: 3px solid var(--seedling-frame);
  }
  .photo--garden {
    left: 431px; top: 279px; width: 218px; height: 296px;
    background: linear-gradient(180deg, #6fd0d8 0%, #74cbc8 28%, #2f7a34 45%, #e0d7c4 55%, #4f9a3a 66%, #a98878 80%, #8f8f8a 100%);
    border: 3px solid var(--teal);
  }
  .photo--site {
    left: 657px; top: 244px; width: 453px; height: 320px;
    background: linear-gradient(180deg, #c4ccd2 0%, #b9c4c8 12%, #5f7a58 22%, #9fa6a6 32%, #cfc8bc 42%, #8c7660 60%, #6e5e4e 72%, #a28a70 100%);
    border: 3px solid var(--frame);
  }
  .website {
    position: absolute; left: 0; right: 0; top: 594px;
    text-align: center; font-size: 31px; font-weight: 700; color: var(--ink);
    padding-right: 30px; line-height: 1.15;
  }
</style>
</head>
<body>
  <main class="billboard">
    <svg class="billboard__backdrop" width="1120" height="656" viewBox="0 0 1120 656" aria-hidden="true">
      <rect width="1120" height="656" fill="var(--panel-grey)"/>
      <polygon points="0,0 828,0 540,252 540,275 0,275" fill="var(--panel-light)"/>
      <polygon points="0,275 657,275 657,588 0,588" fill="var(--panel-light)"/>
      <rect x="0" y="588" width="1120" height="68" fill="var(--panel-band)"/>
    </svg>

    <div class="brand"><span class="brand__dot"></span><span>Ridgeline Depot</span></div>

    <div class="contact">
      <p class="contact__label">Contact Phone :</p>
      <p class="contact__phone">55501-24680</p>
    </div>
    <p class="offer">Sells landscape materials, trees shrubs stone etc.</p>

    <div class="partner partner--excavation">Kestrel<br>Excavation Co.</div>
    <div class="partner partner--homes">Larkspur Homes<br>Construction Co.</div>

    <div class="photo photo--seedlings" role="img" aria-label="Hand holding a young seedling above rows of nursery plants"></div>
    <div class="photo photo--garden" role="img" aria-label="Landscaped garden path leading to a gazebo under palm trees"></div>
    <div class="photo photo--site" role="img" aria-label="Excavation site with an excavator, soil mounds and material stockpiles"></div>

    <p class="website">Website : www.ridgelinedepot.com</p>
  </main>
</body>
</html>
```